Designing a brochures for an educational counseling service provider

We would like a 4 sided design on a 11x8.5 paper, half folded. I have including a sample design we did to give you an idea of what we envision but we welcome creativity to make beautiful looking flyers. Text for the flier is included as well as our logo.
- The most important thing is capturing our audience/market. We will be handing these flies to schools, organizations and individual clients.

www.plorvaeducationalconsultants.example

Target Market(s)

We are targeting international students wanting to study in the U.S and Canada.

Industry/Entity Type

Education

Requirements
Must have
• - Clean and clear
• - Our logo should visible and well placed.
• - Could you the pictures of students, libraries and school buildings or you could use the pictures we already have.
Nice to have
• We would like this to match business cards.

```html
<!DOCTYPE html>
<html lang="en">
<head>
<meta charset="utf-8">
<title>Plorva International Educational Consultants – Brochure Covers</title>
<link rel="stylesheet" href="https://fonts.googleapis.com/css2?family=Open+Sans:wght@300;400;600;700;800&family=Roboto+Condensed:wght@300;400&display=swap">
<style>
  :root {
    --stage: #4a4a4a;
    --paper: #f3f3f3;
    --navy: #0b2a4f;
    --navy-deep: #0a1f38;
    --blue: #1a62ad;
    --blue-light: #2f8fd8;
    --orange: #e8731e;
    --orange-deep: #d4561a;
    --white: #ffffff;
  }
  * { box-sizing: border-box; margin: 0; padding: 0; }
  html, body {
    width: 1200px; height: 1200px; overflow: hidden;
    background: var(--stage);
    font-family: "Open Sans", Arial, sans-serif;
  }
  .spread { position: relative; width: 1200px; height: 1200px; }
  .page {
    position: absolute; top: 190px; width: 530px; height: 820px;
    background: var(--paper); overflow: hidden;
  }
  .page--back { left: 50px; }
  .page--front { left: 620px; }
  .page__art { position: absolute; inset: 0; width: 530px; height: 820px; }
  .page__text { position: absolute; left: 0; right: 0; color: var(--white); }

  /* Back cover */
  .role-line {
    top: 78px; padding-left: 44px; color: var(--blue-light);
    font-weight: 300; font-size: 19px; letter-spacing: 0.5px;
  }
  .role-title {
    top: 104px; padding-left: 44px; color: var(--navy);
    font-weight: 800; font-size: 30px; letter-spacing: 1px;
  }
  .contact-heading {
    top: 592px; text-align: center; font-weight: 400; font-size: 22px; letter-spacing: 1px;
  }
  .contact-company { top: 650px; text-align: center; font-weight: 400; font-size: 18px; letter-spacing: 0.5px; }
  .contact-address { top: 679px; text-align: center; font-weight: 300; font-size: 13px; }
  .contact-phone { top: 700px; text-align: center; font-weight: 700; font-size: 30px; letter-spacing: 1px; }
  .contact-email { top: 764px; text-align: center; font-size: 15px; font-weight: 400; }
  .inline-icon { display: inline-block; vertical-align: middle; margin-right: 6px; }

  /* Front cover */
  .brand { top: 68px; padding-left: 44px; display: flex; align-items: center; gap: 14px; }
  .brand__dot { width: 46px; height: 46px; border-radius: 50%; background: var(--blue); flex: none; }
  .brand__name { color: var(--navy); font-weight: 700; font-size: 22px; line-height: 1.15; }
  .tagline {
    top: 558px; padding: 0 40px; text-align: center;
    font-size: 15px; line-height: 1.35; font-weight: 400;
  }
  .services {
    top: 656px; display: flex; justify-content: space-around; padding: 0 18px; list-style: none;
  }
  .service { width: 112px; text-align: center; }
  .service__icon {
    width: 48px; height: 48px; margin: 0 auto 6px; border-radius: 50%;
    background: var(--white); border: 3px solid var(--orange);
    display: flex; align-items: center; justify-content: center;
  }
  .service__label {
    font-family: "Roboto Condensed", "Arial Narrow", sans-serif;
    font-size: 11.5px; font-weight: 400; text-transform: uppercase; letter-spacing: 0.3px;
  }
  .hotline { top: 772px; padding-left: 30px; font-weight: 700; font-size: 24px; letter-spacing: 0.5px; }
  .location-pill {
    top: 748px; left: auto; right: 16px; background: var(--navy);
    border-radius: 12px; padding: 4px 12px; font-size: 9.5px; white-space: nowrap;
  }
</style>
</head>
<body>
<main class="spread">

  <!-- Back cover -->
  <section class="page page--back">
    <svg class="page__art" viewBox="0 0 530 820" aria-hidden="false">
      <defs>
        <linearGradient id="backPhoto" x1="0" y1="0" x2="1" y2="1">
          <stop offset="0" stop-color="#b9b98a"/>
          <stop offset="0.55" stop-color="#d9cbb6"/>
          <stop offset="1" stop-color="#8fa07a"/>
        </linearGradient>
        <linearGradient id="backBlue" x1="0" y1="0" x2="1" y2="0">
          <stop offset="0" stop-color="#0c3d7a"/>
          <stop offset="1" stop-color="#2a82cf"/>
        </linearGradient>
        <linearGradient id="backOrange" x1="0" y1="0" x2="1" y2="0">
          <stop offset="0" stop-color="#d4561a"/>
          <stop offset="1" stop-color="#f08a2a"/>
        </linearGradient>
      </defs>
      <path d="M0,196 Q265,176 530,160 L530,172 Q265,188 0,208 Z" fill="var(--orange)"/>
      <path d="M0,208 Q265,188 530,172 L530,177 Q265,193 0,213 Z" fill="var(--blue)"/>
      <path d="M0,213 Q265,193 530,177 L530,560 Q265,570 0,600 Z" fill="url(#backPhoto)"
            role="img" aria-label="Photo of three smiling teenage girls in sports shirts on a football field"/>
      <path d="M0,600 Q265,570 530,560 L530,620 Q265,630 0,660 Z" fill="var(--navy-deep)"/>
      <path d="M0,660 Q265,630 530,620 L530,735 Q265,745 0,770 Z" fill="url(#backBlue)"/>
      <path d="M0,770 Q265,745 530,735 L530,790 Q265,796 0,812 Z" fill="url(#backOrange)"/>
    </svg>

    <p class="page__text role-line">EXECUTIVE DIRECTOR &amp; INDEPENDENT</p>
    <h2 class="page__text role-title">EDUCATIONAL CONSULTANT</h2>

    <h3 class="page__text contact-heading">CONTACT US</h3>
    <p class="page__text contact-company">Plorva International Educational Consultants, LLC</p>
    <p class="page__text contact-address">
      <svg class="inline-icon" width="9" height="12" viewBox="0 0 9 12"><path d="M4.5,0 A4.5,4.5 0 0 1 9,4.5 C9,8 4.5,12 4.5,12 C4.5,12 0,8 0,4.5 A4.5,4.5 0 0 1 4.5,0 Z" fill="#fff"/><circle cx="4.5" cy="4.5" r="1.7" fill="#1a62ad"/></svg>418 Harlow Road Suite 120, Kestrel Vale, TX 75001
    </p>
    <p class="page__text contact-phone">
      <svg class="inline-icon" width="22" height="18" viewBox="0 0 22 18"><path d="M2,6 Q11,-2 20,6 L17,9 L14,7 L14,5 Q11,4 8,5 L8,7 L5,9 Z" fill="#fff"/><rect x="7" y="11" width="8" height="6" rx="1" fill="#fff"/></svg>555-012-3478
    </p>
    <p class="page__text contact-email">
      <svg class="inline-icon" width="14" height="10" viewBox="0 0 14 10"><rect width="14" height="10" rx="1" fill="#fff"/><path d="M0.5,0.8 L7,5.5 L13.5,0.8" fill="none" stroke="#d4561a" stroke-width="1.2"/></svg>dana@plorvaeducationalconsultants.example
    </p>
  </section>

  <!-- Front cover -->
  <section class="page page--front">
    <svg class="page__art" viewBox="0 0 530 820">
      <defs>
        <linearGradient id="frontPhoto" x1="0" y1="0" x2="1" y2="1">
          <stop offset="0" stop-color="#3a3530"/>
          <stop offset="0.5" stop-color="#8a5a4a"/>
          <stop offset="1" stop-color="#c99a6a"/>
        </linearGradient>
        <linearGradient id="frontBlue" x1="0" y1="0" x2="1" y2="0">
          <stop offset="0" stop-color="#0c3d7a"/>
          <stop offset="1" stop-color="#1f6fc0"/>
        </linearGradient>
        <linearGradient id="frontOrange" x1="0" y1="0" x2="1" y2="0">
          <stop offset="0" stop-color="#e8731e"/>
          <stop offset="1" stop-color="#d4561a"/>
        </linearGradient>
      </defs>
      <path d="M0,200 Q265,186 530,160 L530,172 Q265,198 0,212 Z" fill="var(--orange)"/>
      <path d="M0,212 Q265,198 530,172 L530,177 Q265,203 0,217 Z" fill="var(--blue)"/>
      <path d="M0,217 Q265,203 530,177 L530,510 Q265,520 0,550 Z" fill="url(#frontPhoto)"
            role="img" aria-label="Photo of three students reading together in front of library bookshelves"/>
      <path d="M0,550 Q265,520 530,510 L530,610 Q265,620 0,650 Z" fill="var(--navy-deep)"/>
      <path d="M0,650 Q265,620 530,610 L530,740 Q265,750 0,770 Z" fill="url(#frontBlue)"/>
      <path d="M0,770 Q265,750 530,740 L530,790 Q265,800 0,815 Z" fill="url(#frontOrange)"/>
    </svg>

    <div class="page__text brand">
      <span class="brand__dot"></span>
      <span class="brand__name">Plorva International<br>Educational Consultants</span>
    </div>

    <p class="page__text tagline">A full-service international educational consulting group<br>serving students and families across the globe.</p>

    <ul class="page__text services">
      <li class="service">
        <div class="service__icon">
          <svg width="24" height="24" viewBox="0 0 24 24" fill="none" stroke="#0b2a4f" stroke-width="1.6"><path d="M3,9 L12,3 L21,9 Z"/><path d="M6,10 V18 M10,10 V18 M14,10 V18 M18,10 V18"/><path d="M3,20 H21"/></svg>
        </div>
        <span class="service__label">Boarding Schools</span>
      </li>
      <li class="service">
        <div class="service__icon">
          <svg width="24" height="24" viewBox="0 0 24 24" fill="none" stroke="#0b2a4f" stroke-width="1.6"><path d="M6,3 H15 L19,7 V21 H6 Z"/><path d="M15,3 V7 H19"/><path d="M9,12 H16 M9,15 H16 M9,18 H13"/></svg>
        </div>
        <span class="service__label">College Admission</span>
      </li>
      <li class="service">
        <div class="service__icon">
          <svg width="24" height="24" viewBox="0 0 24 24" fill="none" stroke="#0b2a4f" stroke-width="1.6"><circle cx="8" cy="8" r="3"/><circle cx="16" cy="8" r="3"/><path d="M3,19 Q8,12 13,19 M11,19 Q16,12 21,19"/></svg>
        </div>
        <span class="service__label">Transfer Students</span>
      </li>
      <li class="service">
        <div class="service__icon">
          <svg width="24" height="24" viewBox="0 0 24 24" fill="none" stroke="#0b2a4f" stroke-width="1.6"><path d="M2,9 L12,4 L22,9 L12,14 Z"/><path d="M6,11 V16 Q12,20 18,16 V11"/><path d="M21,9 V15"/></svg>
        </div>
        <span class="service__label">Graduate Students</span>
      </li>
    </ul>

    <p class="page__text hotline">+1-555-012-3478</p>
    <p class="page__text location-pill">Kestrel Vale, Texas &nbsp;|&nbsp; info@plorvaeducationalconsultants.example</p>
  </section>

</main>
</body>
</html>
```